Business Card Design

The business card is for an IT services company with a specialism
in Integration Services Markets are Health, Government and finance, we provide Velmora SOA platforms and CPB Keystone integration. We are developing multi-agency connectivity

Industry/Entity Type

Business

Contact Information for Business Card

Martin Pell
Director

QVRB Ltd Martin.pell@qvrbltd.example

Mobile: +44 (0) 7700900418
Tel: +44 (0) 1632 960372
Website: www.qvrbltd.example

Ashcombe House, Ashcombe Yard, Halbrook SN99 2ZX

Fenwick Harlowe
Health Integration Services

Mobile +44 (0) 07700900527
Tel +44 (0) 1632 960372
Address as above

```html
<!DOCTYPE html>
<html lang="en">
<head>
<meta charset="utf-8">
<title>Martin Pell — Business Card</title>
<link href="https://fonts.googleapis.com/css2?family=Montserrat:wght@800&family=Questrial&display=swap" rel="stylesheet">
<style>
  :root {
    --blue-bright: #3a78f5;
    --blue-deep: #2254cc;
    --paper: #ffffff;
    --ink: #111111;
    --ink-soft: #555555;
    --ink-title: #444444;
    --band-text: #dbe4fb;
  }
  html, body {
    margin: 0;
    padding: 0;
    overflow: hidden;
    background: var(--paper);
  }
  .card {
    position: relative;
    width: 791px;
    height: 1200px;
    background: var(--paper);
    overflow: hidden;
    font-family: "Questrial", sans-serif;
  }
  .top-bar {
    position: absolute;
    left: 0; top: 0;
    width: 100%;
    height: 47px;
    background: var(--blue-bright);
  }
  .identity {
    position: absolute;
    left: 0; top: 292px;
    width: 100%;
    text-align: center;
  }
  .identity__name {
    margin: 0;
    font-size: 94px;
    line-height: 0.92;
    letter-spacing: -1px;
    white-space: nowrap;
  }
  .identity__first {
    font-family: "Montserrat", sans-serif;
    font-weight: 800;
    color: var(--ink);
  }
  .identity__last {
    font-family: "Questrial", sans-serif;
    font-weight: 400;
    color: var(--ink-soft);
  }
  .identity__rule {
    display: block;
    margin: 0 auto;
    width: 600px;
    height: 6px;
    border-radius: 50%;
    background: radial-gradient(ellipse at center, rgba(0,0,0,0.75) 0%, rgba(0,0,0,0.45) 60%, rgba(0,0,0,0) 100%);
  }
  .identity__role {
    margin: 2px 0 0;
    font-size: 29px;
    font-style: italic;
    color: var(--ink-title);
    letter-spacing: 0.5px;
  }
  .contact {
    position: absolute;
    left: 0;
    width: 100%;
    display: flex;
    align-items: center;
  }
  .contact--address { top: 650px; height: 187px; background: var(--blue-deep); }
  .contact--web { top: 837px; height: 187px; background: var(--blue-bright); }
  .contact--phone { top: 1024px; height: 176px; background: var(--blue-deep); }
  .contact__icon {
    position: absolute;
    left: 82px;
    width: 94px;
    height: 94px;
  }
  .contact__text {
    position: absolute;
    left: 217px;
    font-size: 26px;
    line-height: 33px;
    color: var(--band-text);
  }
  .contact--web .contact__text { left: 222px; }
  .contact--phone .contact__text { margin-top: 14px; }
</style>
</head>
<body>
<main class="card">
  <div class="top-bar"></div>

  <section class="identity">
    <h1 class="identity__name"><span class="identity__first">MARTIN</span> <span class="identity__last">PELL</span></h1>
    <span class="identity__rule"></span>
    <p class="identity__role">DIRECTOR QVRB LTD</p>
  </section>

  <section class="contact contact--address">
    <svg class="contact__icon" viewBox="0 0 94 94" aria-hidden="true">
      <path d="M47 4 C25 4 18 20 18 32 C18 50 47 90 47 90 C47 90 76 50 76 32 C76 20 69 4 47 4 Z" fill="#fff" stroke="#1a1a1a" stroke-width="2"/>
      <circle cx="47" cy="31" r="14" fill="var(--blue-deep)" stroke="#1a1a1a" stroke-width="2"/>
    </svg>
    <p class="contact__text">Ashcombe House, Ashcombe Yard,<br>Halbrook SN99 2ZX</p>
  </section>

  <section class="contact contact--web">
    <svg class="contact__icon" viewBox="0 0 94 94" aria-hidden="true">
      <circle cx="47" cy="47" r="44" fill="#fff" stroke="#1a1a1a" stroke-width="2"/>
      <g fill="none" stroke="var(--blue-deep)" stroke-width="5">
        <circle cx="47" cy="47" r="34"/>
        <ellipse cx="47" cy="47" rx="15" ry="34"/>
        <line x1="47" y1="13" x2="47" y2="81"/>
        <line x1="13" y1="47" x2="81" y2="47"/>
        <line x1="18" y1="31" x2="76" y2="31"/>
        <line x1="18" y1="63" x2="76" y2="63"/>
      </g>
    </svg>
    <p class="contact__text">www.qvrbltd.example</p>
  </section>

  <section class="contact contact--phone">
    <svg class="contact__icon" viewBox="0 0 94 94" aria-hidden="true">
      <g fill="#fff" stroke="#1a1a1a" stroke-width="2" stroke-linejoin="round">
        <path d="M4 28 C4 14 90 14 90 28 L90 36 L70 36 L68 28 L26 28 L24 36 L4 36 Z"/>
        <path d="M28 30 L66 30 L80 86 L14 86 Z"/>
      </g>
      <g fill="#1a1a1a">
        <rect x="38" y="52" width="5" height="4"/><rect x="45" y="52" width="5" height="4"/><rect x="52" y="52" width="5" height="4"/>
        <rect x="38" y="59" width="5" height="4"/><rect x="45" y="59" width="5" height="4"/><rect x="52" y="59" width="5" height="4"/>
        <rect x="38" y="66" width="5" height="4"/><rect x="45" y="66" width="5" height="4"/><rect x="52" y="66" width="5" height="4"/>
      </g>
    </svg>
    <p class="contact__text">+44 (0) 7700900418<br>+44 (0) 1632 960372</p>
  </section>
</main>
</body>
</html>
```